Volna Beauty Mobile App Design

We need an app design for a new on-demand beauty service app called Volna Beauty. We help customers find and book beauty services on-demand (within 48 hours) or into the future. We would like to see designs that are clean and include the logs colors with dark and light shades of grey.
Design should be clean and modern yet showcase that this is a beauty app. It should beautiful and artful as well.
One set of mockups are attached, another set exists.
Competitors include trimquay.com or lustorio.com
Key: You can change the mockups to be best suited for functionality and design. These are here for content only.
Updates
The designs so far look great! Can you please design the portfolio screen for me to see navigation and a registration page to see your idea of textbox and buttons.
Industry/Entity Type
It Service
Look and feel
Each slider illustrates characteristics of the customer's brand and the style your logo design should communicate.

```html
<!DOCTYPE html>
<html lang="en">
<head>
<meta charset="utf-8">
<title>Volna Beauty – App Screens</title>
<link rel="stylesheet" href="https://fonts.googleapis.com/css2?family=Open+Sans:wght@400;600&display=swap">
<style>
  :root {
    --canvas-bg: #b3bbc6;
    --screen-top: #f4f7fa;
    --screen-bottom: #eef3f6;
    --plum: #6f2a5c;
    --plum-dark: #5e2250;
    --grey-button: #9a9a9a;
    --text-grey: #6d6d6d;
    --text-dark: #222222;
    --link-blue: #3f8ee0;
    --ios-blue: #2f7cf6;
    --field-mint: #5fd9c6;
    --bracket-grey: #8a8a8a;
    --keyboard-bg: #d2d5db;
    --key-bg: #ffffff;
    --key-dark: #acb3bd;
    --frame: #1a1a1a;
  }
  * { box-sizing: border-box; margin: 0; padding: 0; }
  html, body { width: 1200px; height: 580px; overflow: hidden; }
  body {
    background: var(--canvas-bg);
    font-family: "Open Sans", Helvetica, Arial, sans-serif;
    position: relative;
  }
  .screen {
    position: absolute;
    top: 93px;
    width: 222px;
    height: 394px;
    border: 2px solid var(--frame);
    background: linear-gradient(180deg, var(--screen-top), var(--screen-bottom));
    overflow: hidden;
  }
  .screen--splash { left: 74px; }
  .screen--steps { left: 361px; }
  .screen--intro { left: 649px; }
  .screen--login { left: 937px; }

  .backdrop { position: absolute; inset: 0; background: radial-gradient(ellipse at 70% 30%, rgba(236,226,230,.55), transparent 65%); }

  .status-bar {
    position: absolute; top: 0; left: 0; right: 0; height: 12px;
    display: flex; justify-content: space-between; align-items: center;
    padding: 0 5px; font-size: 7px; color: var(--text-dark);
  }
  .status-bar__carrier { display: flex; align-items: center; gap: 3px; }
  .status-bar__battery { display: flex; align-items: center; gap: 2px; }
  .battery-icon { width: 12px; height: 6px; border: 1px solid #333; position: relative; }
  .battery-icon::after { content: ""; position: absolute; left: 0; top: 0; bottom: 0; width: 3px; background: #333; }

  .brand { position: absolute; left: 0; right: 0; text-align: center; color: var(--plum); }
  .brand__name { font-size: 20px; font-weight: 400; letter-spacing: 1px; line-height: 1; }
  .brand__tagline { font-size: 5.5px; color: var(--text-grey); margin-top: 2px; padding-left: 40px; }

  .spinner { position: absolute; left: 102px; top: 286px; }

  .steps-list {
    position: absolute; left: 65px; top: 163px; list-style: none;
    font-size: 9.5px; color: var(--text-grey); line-height: 15.5px;
  }
  .intro-copy {
    position: absolute; left: 32px; right: 22px; top: 140px;
    font-size: 9.5px; line-height: 12.2px; color: var(--text-grey);
  }
  .pager { position: absolute; top: 260px; left: 0; right: 0; display: flex; justify-content: center; gap: 4px; }
  .pager__dot { width: 6px; height: 6px; border-radius: 50%; background: var(--plum); }
  .pager__dot--active { background: transparent; border: 1px solid var(--plum); }

  .button {
    position: absolute; left: 65px; width: 92px; height: 26px; border-radius: 2px;
    display: flex; align-items: center; justify-content: center;
    color: #fff; font-size: 11px; letter-spacing: .3px;
  }
  .button--primary { background: var(--plum); border: 1px solid var(--plum-dark); }
  .button--secondary { background: var(--grey-button); }
  .button--login-top { top: 283px; }
  .button--signup { top: 323px; }
  .artist-link {
    position: absolute; top: 367px; left: 0; right: 0; text-align: center;
    font-size: 7.5px; color: var(--link-blue); text-decoration: underline;
  }

  .nav-bar {
    position: absolute; top: 12px; left: 0; right: 0; height: 26px;
    display: flex; align-items: center; justify-content: space-between;
    padding: 0 6px; font-size: 9.5px; color: var(--ios-blue);
  }
  .nav-bar__back { display: flex; align-items: center; gap: 2px; }
  .nav-bar__title { color: var(--text-dark); position: absolute; left: 0; right: 0; text-align: center; pointer-events: none; }
  .brand--compact .brand__name { font-size: 16px; }
  .brand--compact .brand__tagline { font-size: 5px; padding-left: 34px; }

  .field { position: absolute; left: 45px; width: 133px; }
  .field--username { top: 94px; height: 31px; }
  .field--password { top: 139px; height: 32px; }
  .field__frame { position: absolute; inset: 0; }
  .field__label {
    position: absolute; inset: 0; display: flex; align-items: center; justify-content: center;
    font-size: 10px; color: var(--field-mint); letter-spacing: .3px;
  }
  .button--submit { top: 188px; }
  .forgot-link {
    position: absolute; top: 226px; left: 0; right: 0; text-align: center;
    font-size: 7.5px; color: var(--link-blue); text-decoration: underline;
  }

  .keyboard {
    position: absolute; left: 0; right: 0; bottom: 0; height: 146px;
    background: var(--keyboard-bg); padding: 6px 3px 0;
    display: flex; flex-direction: column; gap: 8px;
  }
  .keyboard__row { display: flex; justify-content: center; gap: 3px; height: 25px; }
  .key {
    width: 19px; background: var(--key-bg); border-radius: 3px;
    box-shadow: 0 1px 0 #8e939a; display: flex; align-items: center; justify-content: center;
    font-size: 12px; color: var(--text-dark);
  }
  .key--dark { background: var(--key-dark); }
  .key--mod { width: 28px; }
  .key--small { width: 22px; font-size: 8px; }
  .key--space { width: 84px; font-size: 9px; }
  .key--return { width: 50px; font-size: 9px; }
  .keyboard__row--third { justify-content: space-between; padding: 0 2px; }
  .keyboard__row--third .letters { display: flex; gap: 3px; }
</style>
</head>
<body>

  <!-- Splash -->
  <section class="screen screen--splash">
    <div class="backdrop" role="img" aria-label="Soft blurred beauty photo backdrop"></div>
    <div class="brand" style="top:165px">
      <div class="brand__name">VOLNA BEAUTY</div>
      <div class="brand__tagline">On Demand Beauty Services</div>
    </div>
    <svg class="spinner" width="18" height="18" viewBox="0 0 18 18" aria-label="Loading">
      <g stroke="#777" stroke-width="1.6" stroke-linecap="round">
        <line x1="9" y1="2" x2="9" y2="5" opacity="1"/>
        <line x1="13.9" y1="4.1" x2="11.8" y2="6.2" opacity=".9"/>
        <line x1="16" y1="9" x2="13" y2="9" opacity=".8"/>
        <line x1="13.9" y1="13.9" x2="11.8" y2="11.8" opacity=".7"/>
        <line x1="9" y1="16" x2="9" y2="13" opacity=".55"/>
        <line x1="4.1" y1="13.9" x2="6.2" y2="11.8" opacity=".45"/>
        <line x1="2" y1="9" x2="5" y2="9" opacity=".35"/>
        <line x1="4.1" y1="4.1" x2="6.2" y2="6.2" opacity=".25"/>
      </g>
    </svg>
  </section>

  <!-- Onboarding: steps -->
  <section class="screen screen--steps">
    <div class="backdrop" role="img" aria-label="Soft blurred beauty photo backdrop"></div>
    <div class="status-bar">
      <span class="status-bar__carrier">●●●●○ NetLink</span>
      <span>11:55 PM</span>
      <span class="status-bar__battery">22% <span class="battery-icon"></span></span>
    </div>
    <div class="brand" style="top:96px">
      <div class="brand__name">VOLNA BEAUTY</div>
      <div class="brand__tagline">On Demand Beauty Services</div>
    </div>
    <ol class="steps-list">
      <li>1 - Pick your look</li>
      <li>2 - Select your date/time</li>
      <li>3 - Pick your artist</li>
      <li>4 - Ready to go!</li>
    </ol>
    <div class="pager">
      <span class="pager__dot pager__dot--active"></span>
      <span class="pager__dot"></span>
      <span class="pager__dot"></span>
      <span class="pager__dot"></span>
    </div>
    <div class="button button--primary button--login-top">Login</div>
    <div class="button button--secondary button--signup">Sign Up</div>
    <div class="artist-link">Artists: Sign up here &gt;&gt;</div>
  </section>

  <!-- Onboarding: intro -->
  <section class="screen screen--intro">
    <div class="backdrop" role="img" aria-label="Soft blurred beauty photo backdrop"></div>
    <div class="status-bar">
      <span class="status-bar__carrier">●●●●○ NetLink</span>
      <span>11:55 PM</span>
      <span class="status-bar__battery">22% <span class="battery-icon"></span></span>
    </div>
    <div class="brand" style="top:96px">
      <div class="brand__name">VOLNA BEAUTY</div>
      <div class="brand__tagline">On Demand Beauty Services</div>
    </div>
    <p class="intro-copy">Lorem ipsum dolor sit amet, consectetur adipisicing elit, sed do eiusmod tempor incididunt ut labore et dolore magna aliqua. Ut enim ad minim veniam, quis nostrud exercitation ullamco laboris nisi ut aliquip ex ea commodo consequat.</p>
    <div class="pager">
      <span class="pager__dot"></span>
      <span class="pager__dot pager__dot--active"></span>
      <span class="pager__dot"></span>
      <span class="pager__dot"></span>
    </div>
    <div class="button button--primary button--login-top">Login</div>
    <div class="button button--secondary button--signup">Sign Up</div>
    <div class="artist-link">Artists: Sign up here &gt;&gt;</div>
  </section>

  <!-- Login -->
  <section class="screen screen--login">
    <div class="backdrop" role="img" aria-label="Soft blurred beauty photo backdrop"></div>
    <div class="status-bar">
      <span class="status-bar__carrier">●●●●○ NetLink</span>
      <span>11:55 PM</span>
      <span class="status-bar__battery">22% <span class="battery-icon"></span></span>
    </div>
    <div class="nav-bar">
      <span class="nav-bar__back">
        <svg width="7" height="11" viewBox="0 0 7 11"><path d="M6 1 L1.5 5.5 L6 10" fill="none" stroke="currentColor" stroke-width="1.5"/></svg>
        Back
      </span>
      <span class="nav-bar__title">Login</span>
      <span>Done</span>
    </div>
    <div class="brand brand--compact" style="top:54px">
      <div class="brand__name">VOLNA BEAUTY</div>
      <div class="brand__tagline">On Demand Beauty Services</div>
    </div>
    <div class="field field--username">
      <svg class="field__frame" width="133" height="31" viewBox="0 0 133 31">
        <path d="M1 10 V1 H40 M93 1 H132 V10 M1 21 V30 H40 M93 30 H132 V21" fill="none" stroke="var(--bracket-grey)" stroke-width="1.3"/>
      </svg>
      <span class="field__label">username</span>
    </div>
    <div class="field field--password">
      <svg class="field__frame" width="133" height="32" viewBox="0 0 133 32">
        <path d="M1 10 V1 H40 M93 1 H132 V10 M1 22 V31 H40 M93 31 H132 V22" fill="none" stroke="var(--bracket-grey)" stroke-width="1.3"/>
      </svg>
      <span class="field__label">password</span>
    </div>
    <div class="button button--primary button--submit">Login</div>
    <div class="forgot-link">Forgot the password?</div>

    <div class="keyboard">
      <div class="keyboard__row">
        <span class="key">Q</span><span class="key">W</span><span class="key">E</span><span class="key">R</span><span class="key">T</span><span class="key">Y</span><span class="key">U</span><span class="key">I</span><span class="key">O</span><span class="key">P</span>
      </div>
      <div class="keyboard__row">
        <span class="key">A</span><span class="key">S</span><span class="key">D</span><span class="key">F</span><span class="key">G</span><span class="key">H</span><span class="key">J</span><span class="key">K</span><span class="key">L</span>
      </div>
      <div class="keyboard__row keyboard__row--third">
        <span class="key key--mod">
          <svg width="11" height="11" viewBox="0 0 11 11"><path d="M5.5 1 L10 6 H7.5 V10 H3.5 V6 H1 Z" fill="#222"/></svg>
        </span>
        <span class="letters">
          <span class="key">Z</span><span class="key">X</span><span class="key">C</span><span class="key">V</span><span class="key">B</span><span class="key">N</span><span class="key">M</span>
        </span>
        <span class="key key--mod key--dark">
          <svg width="14" height="10" viewBox="0 0 14 10"><path d="M4 1 H13 V9 H4 L1 5 Z" fill="#fff"/><path d="M7 3.3 L10 6.7 M10 3.3 L7 6.7" stroke="#999" stroke-width="1"/></svg>
        </span>
      </div>
      <div class="keyboard__row">
        <span class="key key--small key--dark">123</span>
        <span class="key key--small key--dark">
          <svg width="11" height="11" viewBox="0 0 11 11" fill="none" stroke="#333" stroke-width=".9"><circle cx="5.5" cy="5.5" r="4.5"/><ellipse cx="5.5" cy="5.5" rx="2" ry="4.5"/><line x1="1" y1="5.5" x2="10" y2="5.5"/></svg>
        </span>
        <span class="key key--small key--dark">
          <svg width="8" height="11" viewBox="0 0 8 11" fill="none" stroke="#333" stroke-width=".9"><rect x="2.5" y="1" width="3" height="6" rx="1.5"/><path d="M1 5.5 a3 3 0 0 0 6 0 M4 8.5 V10.5"/></svg>
        </span>
        <span class="key key--space">space</span>
        <span class="key key--return key--dark">return</span>
      </div>
    </div>
  </section>

</body>
</html>
```